Bref créative
Lark Hollow Events Business Cards & Stationary
A focus on events. All of them. All aspects of them. Anywhere.
I need double sided standard sized Business Card [3.5" x 2"]
Century Gothic
Professional
Melissa Dorne
CEO or would also like to try putting a function like "meetings + events"
4172 County Road 208
Alder Falls, OR 97999
melissa@larkhollowevents.example
www.larkhollowevents.example
Info on who we are and what we do can be found on our website at www.larkhollowevents.example
Would like to see different options like:
phone.
cell.
email.
also, would like to see some options with this symbol: |
Like:
melissa dorne | lark hollow events
Would like to see the card with and without title.
Also, like the + symbol.
I'd like our business cards to look hip and professional...but want them to have some personality.
Our branding colors are gray, teal, and white. Open to incorporting another sub color as you see fit--possibly taupe, navy, or dark fuscia.
Hoping to see innovative ideas on what is up-and-coming with business cards now for people to take notice.
Our logo is new so we are interested in unique ways to use it.
I would like to try to fit this explanation about our name on the back because I love it. I know this will be tight--do what you need to if you need to cut out a little to get it to fit....but lets see if we can do this on the back. (Or, we could go to the fold-out kind if we have to and then do ubllets of our services on the back.)
In the 1950’s, doctors developed a personality classification that was supposed to help them identify predicators for heart disease. They grouped certain criteria together and labeled that personality, “Type A”. The term has come to have some negative connotations.
From our point of view, while we are an eclectic team of varied personalities and interests, we endeavor to provide type A service.
Does that make us a group of unlikable, over-bearing maniacs? No.
We think the so-called “symptoms” of type A are the same qualifications you want in your event planners:
Type A individuals can be described as time-conscious, competitive, ambitious, business-like perfectionists. They are usually over-achievers who derive a great deal of satisfaction from work and multi-tasking. They drive themselves with deadlines and are often “stress junkies”.
–Quiet Engines: Habits of the Restless Mind, Harold Vance
We proudly don the scarlet letter as a badge of our undying need to deliver services to you on time, in budget, and beyond your expectations. If that ends up leading to heart disease….well, we’ll live with that. If our service prevents your heart attacks, then we’ve done our job.
The colors of the logos are very close but still not quite hitting the mark--the gray is a little greenish and the teal is a little blah. When you're using them, please try other shades of gray and teal.
here is the eps version instead of ai in case that is desireable

```html
<!DOCTYPE html>
<html lang="en">
<head>
<meta charset="utf-8">
<title>Lark Hollow Events – Business Cards</title>
<link href="https://fonts.googleapis.com/css2?family=Questrial&display=swap" rel="stylesheet">
<style>
  :root {
    --stage: #1b1b1c;
    --charcoal-top: #3a3a3b;
    --charcoal-bottom: #141414;
    --teal-top: #2c6a72;
    --teal-bottom: #163c42;
    --strip-dark: #0d0d0d;
    --strip-teal: #0f2c31;
    --ink-light: #ffffff;
    --ink-soft: #cfd6d8;
    --paper: #ffffff;
    --paper-edge: #e6e6e6;
    --body-grey: #6d6d6d;
  }
  * { box-sizing: border-box; margin: 0; padding: 0; }
  html, body {
    width: 1200px; height: 899px; overflow: hidden;
    background: var(--stage);
    font-family: "Questrial", "Century Gothic", sans-serif;
  }
  .sheet { position: relative; width: 1200px; height: 899px; }
  .card {
    position: absolute; width: 380px; height: 212px;
    border-radius: 14px; overflow: hidden;
    box-shadow: 0 6px 18px rgba(0,0,0,.45);
  }
  .card-front { left: 198px; }
  .card-back  { left: 602px; background: var(--paper); border: 1px solid var(--paper-edge); }
  .row-charcoal { top: 226px; }
  .row-teal { top: 486px; }
  .front-charcoal { background: linear-gradient(160deg, var(--charcoal-top), var(--charcoal-bottom) 75%); }
  .front-teal { background: linear-gradient(160deg, var(--teal-top), var(--teal-bottom) 80%); }

  .brand {
    position: absolute; left: 16px; top: 34px;
    display: flex; align-items: center; gap: 7px;
    color: var(--ink-light); font-size: 11px; letter-spacing: 1.4px;
    text-transform: uppercase;
  }
  .brand-dot { width: 9px; height: 9px; background: var(--ink-light); }
  .person {
    position: absolute; right: 18px; top: 50px; text-align: right;
    color: var(--ink-light);
  }
  .person-name { font-size: 20px; line-height: 22px; }
  .person-title { font-size: 8.5px; letter-spacing: 1px; margin-top: 2px; color: var(--ink-soft); }
  .contact {
    position: absolute; left: 16px; top: 124px;
    color: var(--ink-soft); font-size: 8px; line-height: 10.5px; font-style: normal;
  }
  .web-strip {
    position: absolute; left: 0; right: 0; bottom: 0; height: 18px;
    padding-left: 16px; display: flex; align-items: center;
    font-size: 8px; letter-spacing: 1.2px; color: var(--ink-soft);
  }
  .front-charcoal .web-strip { background: var(--strip-dark); }
  .front-teal .web-strip { background: var(--strip-teal); }

  .story {
    position: absolute; left: 18px; right: 18px; top: 14px;
    color: var(--body-grey); font-size: 7.5px; line-height: 9.6px;
  }
  .story p { margin-bottom: 6px; }
</style>
</head>
<body>
<main class="sheet">

  <section class="card card-front front-charcoal row-charcoal">
    <div class="brand"><span class="brand-dot"></span>Lark Hollow Events</div>
    <div class="person">
      <div class="person-name">Melissa Dorne</div>
      <div class="person-title">CEO</div>
    </div>
    <address class="contact">
      4172 County Road 208<br>
      Alder Falls, OR 97999<br>
      P: 541.555.0148<br>
      C: 541.555.0172<br>
      F: 541.555.0190<br>
      E: melissa@larkhollowevents.example
    </address>
    <div class="web-strip">www.larkhollowevents.example</div>
  </section>

  <section class="card card-back row-charcoal">
    <div class="story">
      <p>In the 1950s, doctors sorted a set of traits into one label to study heart health, and the label soon gained a mixed reputation.</p>
      <p>We are a varied team with many interests, yet we aim to give driven, exacting service.</p>
      <p>Does that make us hard to work with? No.</p>
      <p>Those so-called symptoms are the very traits you want in the people planning your event:</p>
      <p>Punctual, focused, ambitious and businesslike, they find real joy in work, juggle many tasks and keep every deadline close.</p>
      <p>We wear that drive with pride, delivering on time, on budget and beyond what you expect.</p>
      <p>If our care keeps your event calm, then we have done our job well.</p>
    </div>
  </section>

  <section class="card card-front front-teal row-teal">
    <div class="brand"><span class="brand-dot"></span>Lark Hollow Events</div>
    <div class="person">
      <div class="person-name">Melissa Dorne</div>
      <div class="person-title">CEO</div>
    </div>
    <address class="contact">
      4172 County Road 208<br>
      Alder Falls, OR 97999<br>
      P: 541.555.0148<br>
      C: 541.555.0172<br>
      F: 541.555.0190<br>
      E: melissa@larkhollowevents.example
    </address>
    <div class="web-strip">www.larkhollowevents.example</div>
  </section>

  <section class="card card-back row-teal">
    <div class="story">
      <p>In the 1950s, doctors sorted a set of traits into one label to study heart health, and the label soon gained a mixed reputation.</p>
      <p>We are a varied team with many interests, yet we aim to give driven, exacting service.</p>
      <p>Does that make us hard to work with? No.</p>
      <p>Those so-called symptoms are the very traits you want in the people planning your event:</p>
      <p>Punctual, focused, ambitious and businesslike, they find real joy in work, juggle many tasks and keep every deadline close.</p>
      <p>We wear that drive with pride, delivering on time, on budget and beyond what you expect.</p>
      <p>If our care keeps your event calm, then we have done our job well.</p>
    </div>
  </section>

</main>
</body>
</html>
```